Bold Cover needed for a book on Workplace Bullying

I need a book cover design for a book titled, “Iron Silence?” The book recounts my story of bullying in the workplace. It also includes chapters on how readers can minimize/stop workplace bullying, write an effective complaint, and ensure their own mental wellbeing.
I am looking for a bold design using red and black, and possibly distressed lettering. The covers of other books dealing with this subject do not reflect my vision. They are often too childish or look too academic. This book needs to stress the serious nature of a toxic workplace, while appealing to readers experiencing a similar situation. I’d like the cover to reflect the mental anguish associated with workplace bullying (hence the distressed lettering).
I have included a cover that appeals to me (although the coloring is wrong). That said, I am also very happy (and excited) to see your creative input!
On the cover, it should have the following:
Title: Iron Silence?
Subtitle: How the Harbour Works Department Condones Bullying & Ruins Lives
Author: Owen Frick
Other relevant details:
Book size: 5.5” x 8.5”
Back cover will have a blurb, author picture/short bio, and barcode
The blurb on the back cover reads:
Undermining, intimidation and threats
Despite the Department of Harbour Works allegedly holding a zero tolerance for bullying, these behaviours were an everyday occurrence in at least one workplace. Even after a decade of complaints, numerous witnesses and physical proof, the department failed to act. Instead, they looked the other way, allowing one powerful and well-connected individual to end careers and ruin lives.
After being targeted, one teacher resolved to put an end to the abuse experienced by more than fifty employees. His startling story reveals the relentless bullying, mental health ramifications, and insidious tactics used to cover up the corrosive behaviour.
Those who have experienced a toxic workplace will also find much needed support and guidance, intended to minimise suffering and detail a clear way forward. Chapters include dealing with bullying in the workplace, how to lodge a successful complaint, and how to stay sane during any potential legal action.

```html
<!DOCTYPE html>
<html lang="en">
<head>
<meta charset="utf-8">
<title>Iron Silence? — Owen Frick</title>
<link href="https://fonts.googleapis.com/css2?family=Bebas+Neue&display=swap" rel="stylesheet">
<style>
  :root {
    --ink-white: #ffffff;
    --cover-red: #6a0c0c;
    --cover-deep: #2a0303;
    --stamp-red: #9c0f0f;
  }
  html, body {
    margin: 0;
    padding: 0;
    overflow: hidden;
    background: var(--cover-deep);
  }
  .cover {
    position: relative;
    width: 776px;
    height: 1200px;
    overflow: hidden;
    font-family: "Bebas Neue", "Oswald", sans-serif;
    color: var(--ink-white);
    background:
      radial-gradient(ellipse 60% 40% at 30% 20%, rgba(0,0,0,0.35), transparent 70%),
      radial-gradient(ellipse 50% 35% at 75% 85%, rgba(0,0,0,0.4), transparent 70%),
      radial-gradient(ellipse 70% 30% at 50% 100%, rgba(0,0,0,0.45), transparent 70%),
      repeating-linear-gradient(45deg, rgba(0,0,0,0.12) 0 1px, transparent 1px 3px),
      repeating-linear-gradient(-45deg, rgba(0,0,0,0.12) 0 1px, transparent 1px 3px),
      var(--cover-red);
  }
  .hand-artwork {
    position: absolute;
    left: 70px;
    top: 200px;
    width: 680px;
    height: 640px;
    background: radial-gradient(ellipse 50% 50% at 50% 55%, rgba(156,15,15,0.85), rgba(120,10,10,0.5) 55%, transparent 75%);
  }
  .spread {
    position: absolute;
    display: flex;
    justify-content: space-between;
    margin: 0;
    font-weight: 400;
    line-height: 1;
  }
  .title-main {
    left: 56px;
    right: 56px;
    top: 20px;
    font-size: 322px;
  }
  .title-sub {
    left: 58px;
    right: 56px;
    top: 306px;
    font-size: 130px;
  }
  .subtitle {
    position: absolute;
    left: 388px;
    top: 790px;
    margin: 0;
    width: 700px;
    transform: translate(-50%, -50%) rotate(-19.5deg);
    font-weight: 400;
    font-size: 52px;
    line-height: 0.98;
    text-align: center;
    letter-spacing: 0.5px;
  }
  .subtitle span { display: block; }
  .author {
    left: 54px;
    right: 56px;
    top: 1066px;
    font-size: 118px;
  }
</style>
</head>
<body>
  <div class="cover">
    <div class="hand-artwork" role="img" aria-label="Distressed red handprint stamped with the word 'Enough'"></div>

    <h1 class="spread title-main" aria-label="Iron">
      <span>I</span><span>R</span><span>O</span><span>N</span>
    </h1>
    <h1 class="spread title-sub" aria-label="Silence">
      <span>S</span><span>I</span><span>L</span><span>E</span><span>N</span><span>C</span><span>E</span>
    </h1>

    <h2 class="subtitle">
      <span>How the Harbour Works Department</span>
      <span>Condones Bullying &amp; Ruins Lives</span>
    </h2>

    <p class="spread author" aria-label="Owen Frick">
      <span>O</span><span>W</span><span>E</span><span>N</span><span>&nbsp;</span><span>F</span><span>R</span><span>I</span><span>C</span><span>K</span>
    </p>
  </div>
</body>
</html>
```